Plumweave Inc. Website & Korvix Apps Landing Pages

We need a web site design for our company. We develop software and do various consultant projects for our clients. Our products focus on the mobile platform, mainly the Korvix (business, games, social, etc.). We want to communicate that our software is simple and good as candy. The web pages should be fun to look at not loosing seriousness and credibility. Web 2.0 style and 960 grid system a must. We are opened to any overall site colour scheme suggestions (look at the sites we like below).

Must haves:
- Our logo should be seen on the site and look great on it :-) (preview attached below)
- Main home page and app landing page.
- Section links/tabs on the home page (home,apps,support,blog,contact,about)
- No text in images
- Style sheet

Looks we like:
- http://x7k3lmq9pwrtzv.pixelmoorvault.net/412_Zelto_Site/final_large.jpg
- http://x7k3lmq9pwrtzv.pixelmoorvault.net/Premium_71_Illustrative_Korvix_Landing_Page/final.jpg
- http://grelmwick.com/
- http://dorniply.ca/
- http://quatzel.com/

Industry/Entity Type

Business

Requirements
Must have
• - Company logo should look great on pages.
• - Main home page and app landing page.
• - Section links/tabs on the home page (home,apps,support,blog,contact,about)
• - Web 2.0 style.
• - 960 grid system (12 col, 16 col).
• - Sliced ann optmized
• - Exported in all major formats (psd,ai,eps,png,jpeg,etc)
• - Style sheet
Should not have
• - Text in images

```html
<!DOCTYPE html>
<html lang="en">
<head>
<meta charset="utf-8">
<title>Plumweave — Mobile Application Development</title>
<link href="https://fonts.googleapis.com/css2?family=Source+Sans+3:wght@400;600&family=Arimo:wght@400;700&display=swap" rel="stylesheet">
<style>
:root{
  --dark:#2b3032;
  --dark-2:#23282a;
  --dark-3:#1e2224;
  --light:#f3f3f3;
  --text:#555;
  --muted:#8a8f91;
  --white:#fff;
  --red:#c8190c;
  --orange:#ff7a00;
  --line:#41484a;
}
*{box-sizing:border-box;margin:0;padding:0}
html,body{width:1149px;height:1200px;overflow:hidden}
body{position:relative;background:var(--light);font-family:"Arimo",Arial,sans-serif;color:var(--text)}
.abs{position:absolute}
.heading{font-family:"Source Sans 3",Arial,sans-serif}

/* header */
.site-header{left:0;top:0;width:1149px;height:88px;background:linear-gradient(#33393b,var(--dark-2));border-bottom:1px solid #15191a}
.logo{left:116px;top:22px;font-family:"Source Sans 3",Arial,sans-serif;font-weight:600;font-size:34px;color:var(--white);display:flex;align-items:center;gap:8px}
.logo-dot{width:14px;height:14px;border-radius:50%;background:var(--red)}
.call-us{right:116px;top:8px;font-size:12px;color:var(--muted)}
.call-us b{color:#a9adae;font-weight:700}
.main-nav{right:116px;top:36px;display:flex;gap:6px;font-family:"Source Sans 3",Arial,sans-serif;font-size:15px}
.main-nav a{color:var(--white);text-decoration:none;padding:4px 9px;border-radius:8px;margin-left:22px}
.main-nav a.active{background:#464c4e;margin-left:0}

/* hero */
.hero{left:0;top:89px;width:1149px;height:330px;background:radial-gradient(ellipse at 70% 30%,#ffb000 0%,#ff8a00 35%,#f25a00 60%,#d62a05 100%);overflow:hidden}
.hero-title{left:115px;top:72px;font-size:34px;line-height:34px;font-weight:600;color:var(--white)}
.hero-rule{left:115px;top:167px;width:400px;height:1px;background:linear-gradient(90deg,rgba(255,255,255,.5),rgba(255,255,255,0))}
.hero-sub{left:115px;top:192px;color:var(--white);font-size:19px}
.hero-sub2{left:115px;top:219px;color:var(--white);font-size:24px}
.slider-dots{left:115px;top:291px;display:flex;gap:20px}
.slider-dots span{width:15px;height:15px;border-radius:50%;background:rgba(140,20,0,.45);box-shadow:inset 0 1px 2px rgba(0,0,0,.4)}
.slider-dots span.on{background:radial-gradient(circle at 50% 40%,#fff,#ff6a3a 60%,#c22)}
.hero-visual{left:600px;top:28px;width:300px;height:290px;border-radius:22px;background:linear-gradient(135deg,#3a3d40,#15171a 60%,#4a4d50)}

/* welcome */
.welcome-title{left:115px;top:442px;font-size:30px;color:#111}
.welcome-text{left:115px;top:487px;width:490px;font-size:13px;line-height:23px;text-align:justify;color:#555}

/* latest project */
.latest{left:643px;top:448px;width:392px;height:217px;border-radius:6px;background:linear-gradient(#3b4244,#262b2d);box-shadow:0 12px 14px -10px rgba(0,0,0,.35)}
.latest-title{left:22px;top:16px;font-size:26px;font-weight:600;color:var(--white)}
.latest-name{left:23px;top:56px;font-size:12px;color:var(--red)}
.latest-text{left:23px;top:73px;width:225px;font-size:10.5px;line-height:16.3px;color:#b9bdbe}
.latest-text a{color:var(--white)}
.latest-shot{left:255px;top:25px;width:115px;height:183px;background:linear-gradient(#dfe6ee,#b9c3cc 70%,#3c4346)}

/* case study */
.case{left:115px;top:696px;width:919px;height:242px;border:1px solid #e2e2e2;border-radius:6px;background:linear-gradient(#f9f9f9,#f1f1f1)}
.case-phone{left:57px;top:24px;width:98px;height:186px;border-radius:14px;background:linear-gradient(160deg,#5a5d60,#0d0f12 40%,#1c2a3c 70%,#2a2d30)}
.case-title{left:232px;top:22px;font-size:26px;color:#111}
.case-all{right:28px;top:28px;font-size:12px;color:#222;text-decoration:underline}
.case-name{left:234px;top:67px;font-size:18px;color:var(--red)}
.case-text{left:234px;top:94px;width:620px;font-size:12px;line-height:21px;text-align:justify;color:#555}
.btn{height:25px;padding:0 13px;border-radius:6px;font-size:12px;display:flex;align-items:center;border:1px solid #d5d5d5}
.btn-read{left:235px;top:187px;background:linear-gradient(#fff,#e4e4e4);color:#222;font-weight:700}
.btn-demo{left:329px;top:187px;background:#f6f6f6;color:#c8c8c8;font-weight:700}
.arrow{top:105px}
.arrow-left{left:192px}
.arrow-right{right:32px}

/* footer */
.footer{left:0;top:970px;width:1149px;height:196px;background:var(--dark);border-top:1px solid #1b1f20}
.col-title{font-size:20px;color:var(--white);top:22px}
.col-list{top:56px;list-style:none;font-size:12px;line-height:24px;color:var(--muted);letter-spacing:.3px}
.col-rule{top:24px;width:1px;height:140px;background:var(--line)}
.field{height:26px;width:168px;border:1px solid #4a5153;border-radius:8px;background:#22272a;color:#a9adae;font-size:12px;padding:5px 11px}
.subscribe{left:690px;top:88px;height:26px;padding:0 13px;border-radius:6px;background:linear-gradient(#454b4d,#2c3133);border:1px solid #1b1f20;color:#e8e8e8;font-size:12px;font-weight:700;display:flex;align-items:center}
.unsub{left:970px;top:93px;font-size:11px;color:#b9bdbe;text-decoration:underline}
.footer-rule{left:690px;top:130px;width:343px;height:1px;background:var(--line)}
.follow{left:690px;top:143px;font-size:19px;color:var(--white)}
.social{left:775px;top:145px;display:flex;gap:8px}
.social span{width:19px;height:19px;border-radius:3px;background:#c9cccd}
.bottom-bar{left:0;top:1166px;width:1149px;height:34px;background:var(--dark-3)}
.copyright{left:112px;top:11px;font-size:11px;color:var(--muted)}
.badges{left:362px;top:10px;display:flex;gap:3px}
.badges span{width:64px;height:14px;border:1px solid #6a7072;background:#3a4042}
.legal{right:116px;top:11px;font-size:11px;color:var(--muted)}
.legal i{font-style:normal;margin:0 6px}
</style>
</head>
<body>

<header class="site-header abs">
  <div class="logo abs"><span class="logo-dot"></span>plumweave</div>
  <div class="call-us abs">Call Us <b>+11 2345 6789</b></div>
  <nav class="main-nav abs">
    <a class="active" href="#">HOME</a><a href="#">APPS</a><a href="#">SUPPORT</a><a href="#">BLOG</a><a href="#">CONTACT</a><a href="#">ABOUT</a>
  </nav>
</header>

<section class="hero abs">
  <h1 class="hero-title heading abs">Mobile Application<br>Development</h1>
  <div class="hero-rule abs"></div>
  <p class="hero-sub heading abs">We make&nbsp; Professional apps for Mobile Phones</p>
  <p class="hero-sub2 heading abs">Quick and Easy.</p>
  <div class="slider-dots abs"><span></span><span></span><span class="on"></span><span></span><span></span></div>
  <div class="hero-visual abs" role="img" aria-label="Three smartphones showing app home screens"></div>
</section>

<h2 class="welcome-title heading abs">Welcome!</h2>
<p class="welcome-text abs">Curabitur id velit mauris. Aliquam at arcu vitae libero tristique ornare. Nulla ut sem sapien, nec auctor ipsum. Curabitur id velit mauris. Aliquam at arcu vitae libero tristique ornare. Nulla ut sem sapien, nec auctor ipsum. Curabitur id velit mauris. Aliquam at arcu vitae libero tristique ornare. Nulla ut sem sapien, nec auctor ipsum. Aliquam at arcu vitae libero tristique ornare. Curabitur id velit mauris. Aliquam at arcu vitae libero tristique ornare. Nulla ut sem sapien, nec auctor ipsum. Curabitur id velit mauris. Aliquam at arcu vitae libero tristique ornare. Nulla ut sem sapien, nec auctor ipsum.</p>

<aside class="latest abs">
  <h3 class="latest-title heading abs">Latest Project</h3>
  <div class="latest-name abs">Roamly MAPS</div>
  <p class="latest-text abs">Curabitur id velit mauris. Aliquam at arcu vitae libero tristique ornare. Nulla ut sem sapien, nec auctor ipsum. Curabitur id velit mauris. Aliquam at arcu vitae libero tristique ornare. Nulla ut sem sapien, nec auctor ipsum. Curabitur id velit mauris. Aliquam at arcu vitae libero tristique ornare.<br><a href="#">Read more</a></p>
  <div class="latest-shot abs" role="img" aria-label="App screen of a body mass index calculator"></div>
</aside>

<section class="case abs">
  <div class="case-phone abs" role="img" aria-label="Smartphone showing a city guide map app"></div>
  <svg class="arrow arrow-left abs" width="26" height="38" viewBox="0 0 26 38"><path d="M22 3 6 19l16 16" fill="none" stroke="#fff" stroke-width="5" stroke-linecap="round"/><path d="M22 3 6 19l16 16" fill="none" stroke="#ddd" stroke-width="2"/></svg>
  <h3 class="case-title heading abs">Case Study</h3>
  <a class="case-all abs" href="#">Read all case studies</a>
  <div class="case-name abs">Roamly MAPS</div>
  <p class="case-text abs">Curabitur id velit mauris. Aliquam at arcu vitae libero tristique ornare. Nulla ut sem sapien, nec auctor ipsum. Curabitur id velit mauris. Aliquam at arcu vitae libero tristique ornare. Nulla ut sem sapien, nec auctor ipsum. Curabitur id velit mauris. Aliquam at arcu vitae libero tristique ornare. Nulla ut sem sapien, nec auctor ipsum. Aliquam at arcu vitae libero tristique ornare.</p>
  <div class="btn btn-read abs">Read more</div>
  <div class="btn btn-demo abs">Launch App Demo</div>
  <svg class="arrow arrow-right abs" width="26" height="38" viewBox="0 0 26 38"><path d="M4 3l16 16L4 35" fill="none" stroke="#fff" stroke-width="5" stroke-linecap="round"/><path d="M4 3l16 16L4 35" fill="none" stroke="#ddd" stroke-width="2"/></svg>
</section>

<footer class="footer abs">
  <h4 class="col-title heading abs" style="left:116px">Technology Expertise</h4>
  <ul class="col-list abs" style="left:118px">
    <li>Korvix Development</li><li>Native, Web, Hybrid</li><li>Mobile App Development</li><li>Game Development</li><li>Business Software Development</li>
  </ul>
  <div class="col-rule abs" style="left:361px"></div>
  <h4 class="col-title heading abs" style="left:390px">Solutions</h4>
  <ul class="col-list abs" style="left:392px">
    <li>Mobile Application Development</li><li>Application Support</li><li>Mobile Application Upgrade</li><li>Navigation App Support</li><li>Mobile Application Outsource</li>
  </ul>
  <div class="col-rule abs" style="left:650px"></div>
  <h4 class="col-title heading abs" style="left:690px">Newsletter</h4>
  <div class="field abs" style="left:689px;top:53px">Name</div>
  <div class="field abs" style="left:865px;top:53px">E-mail</div>
  <div class="subscribe abs">Subscribe</div>
  <a class="unsub abs" href="#">Unsubscribe</a>
  <div class="footer-rule abs"></div>
  <div class="follow heading abs">Follow Us!</div>
  <div class="social abs"><span></span><span></span><span></span><span></span></div>
</footer>

<div class="bottom-bar abs">
  <div class="copyright abs">Copyright © 2010 Plumweave. All rights reserved.</div>
  <div class="badges abs"><span></span><span></span></div>
  <div class="legal abs">Privacy Policy<i>|</i>Contact Us<i>|</i>Disclaimer<i>|</i>Terms of Use</div>
</div>

</body>
</html>
```